Whiskey Glass Packaging Design Project

I require a package design for my products - Whiskey Tasting glasses ( Set of 4) I will be selling on the Brindlecart USA platform. Must be of high quality, something that the customer will be very impressed with after opening once it arrives at their doorstop. To get an idea of competition please take a look on Brindlecart.example and do a search on Whiskey Glasses - Scotch Glasses. The competition is very good so we require something that will be better than them. We have a home and kitchen brand that caters to an audience that appreciate fine whiskey / oak barrels / cigars ... I can provide logo and content to be placed on box as well as dine line.

Target Market(s)

Men who love all things about Whiskey / Business / Cigars. Men / Women / Wives / Husbands who are looking to buy gifts for Husband / Partner .

Requirements
Must have
• On one side of the box we would like for the following wording to be included.
The GARVELOT snifter glass is one of the ideal glasses that all enthusiasts will swear by. The glass is a type of stemware, a short - stemmed glass whose vessel has a wide bottom and a relatively narrow top. It is mostly used to serve aged brown Scotch / Whiskey, Bourbon and Brandy.
It's simply a matter of raising the glass to take in a whiff of the aromas before taking a sip. We hope the graceful design of this GARVELOT Whiskey glass adds a nice touch of class to the presentation of your favourite drop ! Enjoy !
Nice to have
• Elegant, soothing and relaxing feel.
Should not have
• Nothing aggressive, racist, homosexual / anti gay .

```html
<!DOCTYPE html>
<html lang="en">
<head>
<meta charset="utf-8">
<title>GARVELOT – Whiskey Glass Box Dieline</title>
<link rel="stylesheet" href="https://fonts.googleapis.com/css2?family=Montserrat:wght@400;500&display=swap">
<style>
  :root {
    --paper: #ffffff;
    --board: #000000;
    --amber: #ff8000;
    --amber-deep: #7a3a00;
  }
  html, body {
    margin: 0;
    padding: 0;
    width: 1200px;
    height: 640px;
    overflow: hidden;
    background: var(--paper);
  }
  .dieline-sheet {
    position: relative;
    width: 1200px;
    height: 640px;
    overflow: hidden;
    font-family: "Montserrat", Arial, sans-serif;
    color: var(--amber);
  }
  .dieline-shape {
    position: absolute;
    inset: 0;
    width: 1200px;
    height: 640px;
  }
  .dieline-shape .board { fill: var(--board); }
  .dieline-shape .slit { stroke: var(--paper); stroke-width: 2; }

  .wordmark {
    position: absolute;
    margin: 0;
    font-weight: 400;
    white-space: nowrap;
    text-align: center;
    line-height: 1;
  }
  .wordmark--side {
    left: 160px;
    width: 120px;
    top: 283px;
    font-size: 9px;
    letter-spacing: 0.42em;
    text-indent: 0.42em;
  }
  .wordmark--side-flipped {
    left: 160px;
    width: 120px;
    top: 143px;
    font-size: 9px;
    letter-spacing: 0.42em;
    text-indent: 0.42em;
    transform: rotate(180deg);
  }
  .wordmark--panel {
    left: 628px;
    width: 120px;
    top: 335px;
    font-size: 11px;
    letter-spacing: 0.5em;
    text-indent: 0.5em;
  }
  .wordmark--hero {
    top: 283px;
    font-size: 47px;
    font-weight: 500;
    letter-spacing: 0.02em;
  }
  .wordmark--hero-front { left: 353px; width: 270px; }
  .hero-clip {
    position: absolute;
    left: 893px;
    top: 230px;
    width: 272px;
    height: 160px;
    overflow: hidden;
  }
  .hero-clip .wordmark--hero { left: 0; top: 53px; width: 282px; }

  .glass-artwork {
    position: absolute;
    left: 188px;
    top: 309px;
    width: 65px;
    height: 89px;
    border-radius: 14px 14px 20px 20px;
    background: radial-gradient(ellipse at 50% 45%, var(--amber-deep), #1a0c00 75%);
  }

  .side-copy {
    position: absolute;
    left: 761px;
    top: 265px;
    width: 112px;
    margin: 0;
    font-size: 6.1px;
    line-height: 7.35px;
    text-align: justify;
    hyphens: manual;
  }
  .side-copy p { margin: 0 0 7.35px; }
</style>
</head>
<body>
<main class="dieline-sheet">
  <svg class="dieline-shape" viewBox="0 0 2560 1376" preserveAspectRatio="none" aria-hidden="true">
    <!-- main body -->
    <rect class="board" x="175" y="212" width="2301" height="968"/>
    <rect class="board" x="2470" y="510" width="15" height="372"/>
    <!-- glue tab -->
    <polygon class="board" points="91,557 176,507 176,885 91,835"/>
    <!-- top flaps -->
    <polygon class="board" points="209,214 209,170 246,133 448,133 468,153 489,133 691,133 728,170 728,214"/>
    <rect class="board" x="761" y="138" width="565" height="110" rx="32"/>
    <polygon class="board" points="1359,214 1359,170 1396,133 1598,133 1618,153 1639,133 1841,133 1878,170 1878,214"/>
    <rect class="board" x="1910" y="138" width="566" height="110" rx="32"/>
    <!-- bottom flaps -->
    <polygon class="board" points="209,1178 209,1223 246,1260 448,1260 468,1240 489,1260 691,1260 728,1223 728,1178"/>
    <rect class="board" x="761" y="1145" width="565" height="110" rx="32"/>
    <polygon class="board" points="1359,1178 1359,1223 1396,1260 1598,1260 1618,1240 1639,1260 1841,1260 1878,1223 1878,1178"/>
    <rect class="board" x="1910" y="1145" width="566" height="110" rx="32"/>
    <!-- flap slits -->
    <line class="slit" x1="468" y1="150" x2="468" y2="175"/>
    <line class="slit" x1="1618" y1="150" x2="1618" y2="175"/>
    <line class="slit" x1="468" y1="1218" x2="468" y2="1243"/>
    <line class="slit" x1="1618" y1="1218" x2="1618" y2="1243"/>
  </svg>

  <p class="wordmark wordmark--side-flipped">GARVELOT</p>
  <p class="wordmark wordmark--side">GARVELOT</p>
  <div class="glass-artwork" role="img" aria-label="Line drawing of a snifter whiskey glass in amber"></div>

  <p class="wordmark wordmark--hero wordmark--hero-front">GARVELOT</p>

  <p class="wordmark wordmark--panel">GARVELOT</p>

  <div class="side-copy">
    <p>The GARVELOT snifter glass is one of the ideal glasses that all enthusi&shy;asts will swear by. The glass is a type of stemware, a short - stemmed glass whose vessel has a wide bottom and a relatively narrow top. It is mostly used to serve aged brown Scotch / Whiskey, Bourbon and Brandy.</p>
    <p>It's simply a matter of raising the glass to take in a whiff of the aromas before taking a sip. We hope the graceful design of this GARVELOT Whiskey glass adds a nice touch of class to the presentation of your favourite drop ! Enjoy !</p>
  </div>

  <div class="hero-clip">
    <p class="wordmark wordmark--hero">GARVELOT</p>
  </div>
</main>
</body>
</html>
```